Royal Meadow Hamper company needs a brochure design

We need a brochure design for a new company in Dubai called 'Royal Meadow Hampers'. We already have a logo designed which I have attached and would like to use this and the green/gold/white colours for our brochure. Our company initially will be supplying Royal Meadow Hamper wear of traditional wicker baskets in many designs which hold all the cutlery, crockery and accessories. We will also be selling picnic accessories. We want to purvey a sense of luxury and class in line with our logo. I have attached some photos of the picnicwear. As our products are changing all the time I thought a fold out cover which stays the same and then product cards inserted into the folder which can be changed according to our product changes. I am looking for a fairly simple design and each product card should have at least one photo of the product on it with a spec and description also. On the cover of the folder I would like room to write about the company and what we do, this can be inside or out and may or may not include photos. I have the logo designs in illustrator format and pdf. Please contact if any more information is needed.

Reason: I have extended this deadline as there are some content changes taking place.

```html
<!DOCTYPE html>
<html lang="en">
<head>
<meta charset="utf-8">
<title>Royal Meadow Hampers – Folder Inside Panel</title>
<link href="https://fonts.googleapis.com/css2?family=Gelasio:wght@400&family=Montserrat:wght@600&display=swap" rel="stylesheet">
<style>
  :root {
    --paper: #ffffff;
    --ink-green: #1f3a1c;
    --brand-green: #0f2a12;
    --gold: #c4921f;
    --mark: #1a1a1a;
  }
  html, body {
    margin: 0;
    padding: 0;
    width: 1200px;
    height: 969px;
    overflow: hidden;
    background: var(--paper);
  }
  .sheet {
    position: relative;
    width: 1200px;
    height: 969px;
    background: var(--paper);
  }
  .print-marks {
    position: absolute;
    inset: 0;
  }
  .fold-label {
    position: absolute;
    font-family: Arial, Helvetica, sans-serif;
    font-size: 8px;
    color: var(--mark);
    white-space: nowrap;
  }
  .fold-label--center { left: 514px; top: 0; }
  .fold-label--side { left: 1029px; top: 0; }
  .fold-label--up { left: 567px; top: 6px; }

  .panel {
    position: absolute;
    left: 127px;
    top: 90px;
    width: 316px;
  }
  .brand-name {
    margin: 0;
    padding-top: 15px;
    font-family: "Montserrat", Arial, sans-serif;
    font-weight: 600;
    font-size: 11.5px;
    letter-spacing: 2.4px;
    color: var(--brand-green);
    white-space: nowrap;
  }
  .welcome-title {
    margin: 70px 0 0;
    font-family: "Gelasio", Georgia, serif;
    font-weight: 400;
    font-size: 18.5px;
    color: var(--gold);
  }
  .intro {
    margin-top: 27px;
    font-family: "Gelasio", Georgia, serif;
    font-size: 13.1px;
    line-height: 15.7px;
    color: var(--ink-green);
  }
  .intro p {
    margin: 0 0 7px;
  }
</style>
</head>
<body>
<main class="sheet">
  <svg class="print-marks" width="1200" height="969" viewBox="0 0 1200 969" aria-hidden="true">
    <g stroke="var(--mark)" stroke-width="0.8" fill="none">
      <!-- corner trim lines -->
      <line x1="30" y1="0" x2="30" y2="20"/><line x1="0" y1="30" x2="20" y2="30"/>
      <line x1="1170" y1="0" x2="1170" y2="20"/><line x1="1180" y1="30" x2="1200" y2="30"/>
      <line x1="30" y1="949" x2="30" y2="969"/><line x1="0" y1="939" x2="20" y2="939"/>
      <line x1="1170" y1="949" x2="1170" y2="969"/><line x1="1180" y1="939" x2="1200" y2="939"/>
      <!-- registration targets -->
      <g transform="translate(15 15)"><circle r="5"/><line x1="-8" y1="0" x2="8" y2="0"/><line x1="0" y1="-8" x2="0" y2="8"/></g>
      <g transform="translate(1185 15)"><circle r="5"/><line x1="-8" y1="0" x2="8" y2="0"/><line x1="0" y1="-8" x2="0" y2="8"/></g>
      <g transform="translate(15 953)"><circle r="5"/><line x1="-8" y1="0" x2="8" y2="0"/><line x1="0" y1="-8" x2="0" y2="8"/></g>
      <g transform="translate(1185 953)"><circle r="5"/><line x1="-8" y1="0" x2="8" y2="0"/><line x1="0" y1="-8" x2="0" y2="8"/></g>
      <!-- fold arrows -->
      <line x1="538" y1="9" x2="538" y2="19"/>
      <line x1="1046" y1="9" x2="1046" y2="19"/>
      <line x1="538" y1="945" x2="538" y2="956"/>
      <line x1="1046" y1="945" x2="1046" y2="956"/>
      <line x1="0" y1="721" x2="19" y2="721"/>
      <line x1="1181" y1="721" x2="1200" y2="721"/>
    </g>
    <g fill="var(--mark)">
      <path d="M535.5 18 L540.5 18 L538 22 Z"/>
      <path d="M1043.5 18 L1048.5 18 L1046 22 Z"/>
      <path d="M535.5 947 L540.5 947 L538 943 Z"/>
      <path d="M1043.5 947 L1048.5 947 L1046 943 Z"/>
      <path d="M18 718.5 L18 723.5 L22 721 Z"/>
      <path d="M1182 718.5 L1182 723.5 L1178 721 Z"/>
    </g>
  </svg>
  <span class="fold-label fold-label--center">Center Fold</span>
  <span class="fold-label fold-label--up">UP</span>
  <span class="fold-label fold-label--side">Side Fold</span>

  <section class="panel">
    <p class="brand-name">ROYAL MEADOW HAMPERS</p>
    <h1 class="welcome-title">Welcome to Royal Meadow Hampers!</h1>
    <div class="intro">
      <p>The British love to picnic no matter what the weather and the picnic basket epitomises the British summer. Days spent relaxing with loved ones, dining ‘al fresco’ with a willow basket packed with delicious food is a great British tradition.</p>
      <p>Royal Meadow Hampers offer a range of stylish traditional willow picnic hampers with a contemporary feel. Each basket comes equipped with cutlery, crockery and accessories, everything one would need for a perfect picnic. Having the highest ethical and ecological values, all our baskets are made from sustainable materials and individually handmade by Artisans.</p>
      <p>Alongside our range of picnic baskets we also offer a range of accessories from luxurious rugs to relax on, to stylish cool bags to keep your meals fresh.</p>
      <p>We at Royal Meadow Hampers invite you to enjoy this classically English pastime!</p>
    </div>
  </section>
</main>
</body>
</html>
```